Med Spa business card design with logo

Need a logo design and business card for our new company Verbena Aesthetics Med Spa. We are a medical office that deals with high end clients. We offer them skin care products which include DERMIQ, lip augmentation, and various laser for the skin. I king of like the logo attached, maybe something along those lines but also open to any logo concept.
Updates

Target Market(s)

Out target audience are male and females in the age range of 21-80 years of age

Industry/Entity Type

Medical

Contact Information for Business Card

woukd like front of card to have logo and business name VERBENA AESTHETICS MEDSPA. Back of card employee name and phone number along with instagram logo and user name

Font styles to use
Serif
Sans Serif

Requirements
Must have
• prefer monochromatic look white, black, gold
Should not have
• not too colorful

```html
<!DOCTYPE html>
<html lang="en">
<head>
<meta charset="utf-8">
<title>Verbena Aesthetics Med Spa – Business Card</title>
<link href="https://fonts.googleapis.com/css2?family=Montserrat:wght@400;500;600&display=swap" rel="stylesheet">
<style>
  :root {
    --backdrop: #8a8a8a;
    --card-dark: #111111;
    --card-light: #ffffff;
    --ink-dark: #2b2f33;
    --ink-light: #f4f4f4;
    --accent-rose: #c9a596;
    --muted: #7d8185;
  }
  html, body {
    margin: 0;
    width: 1200px;
    height: 873px;
    overflow: hidden;
    background: var(--backdrop);
    font-family: "Montserrat", sans-serif;
  }
  .canvas {
    width: 1200px;
    height: 873px;
    display: flex;
    align-items: center;
    justify-content: center;
    gap: 60px;
  }
  .card {
    width: 500px;
    height: 286px;
    border-radius: 4px;
    box-shadow: 0 10px 28px rgba(0,0,0,0.28);
    display: flex;
    flex-direction: column;
    align-items: center;
    justify-content: center;
  }
  .card--back {
    background: var(--card-dark);
    color: var(--ink-light);
  }
  .card--front {
    background: var(--card-light);
    color: var(--ink-dark);
  }
  .employee-name {
    font-size: 19px;
    font-weight: 600;
    margin: 0 0 14px;
    letter-spacing: 0.2px;
  }
  .contact-row {
    display: flex;
    gap: 34px;
    font-size: 13px;
    font-weight: 400;
  }
  .contact-item {
    display: flex;
    align-items: center;
    gap: 7px;
  }
  .handle-mark {
    width: 12px;
    height: 12px;
    border: 1.5px solid var(--ink-light);
    border-radius: 3px;
    box-sizing: border-box;
  }
  .brand-dot {
    width: 34px;
    height: 34px;
    border-radius: 50%;
    background: var(--accent-rose);
    margin-bottom: 10px;
  }
  .brand-name {
    font-size: 44px;
    font-weight: 500;
    letter-spacing: 12px;
    margin: 0 0 6px 12px;
    line-height: 1;
  }
  .brand-tagline {
    font-size: 9px;
    color: var(--muted);
    letter-spacing: 1.2px;
    margin: 0;
  }
</style>
</head>
<body>
  <main class="canvas">
    <section class="card card--back">
      <p class="employee-name">Dr. Marcus Hale</p>
      <div class="contact-row">
        <span class="contact-item"><span class="handle-mark"></span>@verbenact</span>
        <span class="contact-item">
          <svg width="12" height="12" viewBox="0 0 24 24" aria-hidden="true">
            <path fill="#f4f4f4" d="M6.6 10.8a15.1 15.1 0 0 0 6.6 6.6l2.2-2.2a1 1 0 0 1 1-.25 11.4 11.4 0 0 0 3.6.57 1 1 0 0 1 1 1V20a1 1 0 0 1-1 1A17 17 0 0 1 3 4a1 1 0 0 1 1-1h3.5a1 1 0 0 1 1 1c0 1.25.2 2.45.57 3.57a1 1 0 0 1-.25 1z"/>
          </svg>+1 555-014-2290
        </span>
      </div>
    </section>
    <section class="card card--front">
      <span class="brand-dot"></span>
      <h1 class="brand-name">verbena</h1>
      <p class="brand-tagline">Medical Aesthetics Med Spa</p>
    </section>
  </main>
</body>
</html>
```